BUilding Fascia Signage

I got the logo, now, I want to design the Fascia Signage for my shop.
Fasica signage is 5565mm x 470mmH
Need idea how to put the logo, text, colour to the fascia signage.
need something catching.
can add more decorate line.
may try with Black background and white background

Design & Build

```html
<!DOCTYPE html>
<html lang="en">
<head>
<meta charset="utf-8">
<title>VKR Building Group – Fascia Signage Concepts</title>
<link rel="stylesheet" href="https://fonts.googleapis.com/css2?family=Archivo+Black&family=Montserrat:wght@500&display=swap">
<style>
  :root {
    --page: #ffffff;
    --fascia: #000000;
    --accent: #3d87f5;
    --ink-light: #ffffff;
  }
  * { margin: 0; padding: 0; box-sizing: border-box; }
  html, body {
    width: 1200px;
    height: 729px;
    overflow: hidden;
    background: var(--page);
  }
  .canvas {
    position: relative;
    width: 1200px;
    height: 729px;
  }
  .fascia {
    position: absolute;
    width: 994px;
    height: 84px;
    background: var(--fascia);
    display: flex;
    align-items: center;
  }
  .fascia--top { left: 113px; top: 121px; }
  .fascia--middle { left: 103px; top: 315px; }
  .fascia--lower { left: 141px; top: 540px; width: 985px; }

  .brand-mark {
    width: 22px;
    height: 22px;
    background: var(--accent);
    flex: none;
  }
  .brand-name {
    font-family: "Archivo Black", "Arial Black", sans-serif;
    font-size: 38px;
    line-height: 1;
    letter-spacing: 1px;
    color: var(--ink-light);
    text-transform: uppercase;
    white-space: nowrap;
    flex: none;
  }
  .rule {
    height: 2px;
    background: var(--accent);
    flex: none;
  }
  .tagline {
    display: flex;
    align-items: center;
    gap: 12px;
    flex: none;
  }
  .tagline__rule {
    width: 62px;
    height: 2px;
    background: var(--ink-light);
  }
  .tagline__text {
    font-family: "Montserrat", "Helvetica Neue", sans-serif;
    font-weight: 500;
    font-size: 19px;
    letter-spacing: 3px;
    color: var(--ink-light);
    white-space: nowrap;
  }

  /* Concept A: mark leading, name, tagline right */
  .fascia--top { padding: 0 26px 0 40px; gap: 20px; }
  .fascia--top .tagline { margin-left: auto; }

  /* Concept B: name flanked by accent rules */
  .fascia--middle,
  .fascia--lower { padding: 0 26px 0 30px; gap: 18px; }
  .fascia--middle .tagline,
  .fascia--lower .tagline { margin-left: auto; }
</style>
</head>
<body>
<main class="canvas">

  <section class="fascia fascia--top" aria-label="Fascia concept A">
    <span class="rule" style="width:48px"></span>
    <span class="brand-mark"></span>
    <h1 class="brand-name">VKR Building Group</h1>
    <div class="tagline">
      <span class="tagline__rule"></span>
      <span class="tagline__text">DESIGN &amp; BUILD</span>
      <span class="tagline__rule"></span>
    </div>
  </section>

  <section class="fascia fascia--middle" aria-label="Fascia concept B">
    <h2 class="brand-name">VKR Building Group</h2>
    <span class="rule" style="width:52px"></span>
    <div class="tagline">
      <span class="tagline__rule"></span>
      <span class="tagline__text">DESIGN &amp; BUILD</span>
      <span class="tagline__rule"></span>
    </div>
  </section>

  <section class="fascia fascia--lower" aria-label="Fascia concept B, shopfront application">
    <h2 class="brand-name">VKR Building Group</h2>
    <span class="rule" style="width:52px"></span>
    <div class="tagline">
      <span class="tagline__rule"></span>
      <span class="tagline__text">DESIGN &amp; BUILD</span>
      <span class="tagline__rule"></span>
    </div>
  </section>

</main>
</body>
</html>
```